PIPE RELINING COMPANY NEEDS A NEW INFORMATIVE FLYER CREATED

We are a company that sells a service to residential homeowners (using a particular state of the art international product) and we need to refresh our A4 tri- fold flyer (z fold 6 pages). The layout needs to include pictures, heading and text boxes, but be simple and clean cut at the same time.

The front of the flyer must have the attached picture of the pipe under the house, logo and website.

This flyer is going to be given to clients and to leave with them when we quote for work.

Our colour scheme is black, white, red. A highlight colour if needed (in small amounts) could be 100% cyan and also a bright orange.

I have attached the copy of the text and this can be spread out throughout the brochure.

We are a professional and industry leading company so it needs to be professional, clean cut but with a modern edge.

Target Market(s)

HOMEOWNERS

Industry/Entity Type

It Company

Font styles to use
Sans Serif

Colors
ec1f27
ffffff
000000
f37122

Requirements
Must have
• PROFESSINAL, MODERN
• USE OF BLACK, RED AND WHITE - REFER LOGO
Should not have
• BE CLUTTERED

```html
<!DOCTYPE html>
<html lang="en">
<head>
<meta charset="utf-8">
<title>Pipewell Pipe Relining – Tri-fold Flyer</title>
<link href="https://fonts.googleapis.com/css2?family=Lato:wght@400;700;900&display=swap" rel="stylesheet">
<style>
:root{
  --red:#d7141c;
  --red-bright:#ec1f27;
  --orange:#f37122;
  --black:#000;
  --white:#fff;
  --rule:#3a3a3a;
}
*{margin:0;padding:0;box-sizing:border-box}
html,body{width:1200px;height:1200px;overflow:hidden;background:var(--white)}
body{font-family:'Lato',sans-serif;color:var(--white)}
.stage{position:absolute;left:0;top:0;width:1280px;height:1280px;transform:scale(.9375);transform-origin:0 0}
.sheet{position:absolute;left:220px;width:840px;height:594px;overflow:hidden;background:var(--black)}
.sheet--outer{top:28px;background:linear-gradient(90deg,#000 0%,#000 40%,#1c1c1c 66%,#000 67%)}
.sheet--inner{top:645px;background:var(--red)}
.sheet-bg{position:absolute;inset:0;width:840px;height:594px}
.block{position:absolute}
.tag{display:inline-block;position:relative;background:var(--orange);color:var(--white);font-weight:700;font-size:14px;line-height:24px;padding:0 14px 0 12px;clip-path:polygon(0 0,100% 0,calc(100% - 10px) 100%,0 100%)}
.tag--white{background:var(--white);color:var(--red)}
.copy{font-size:15px;line-height:17px}
.copy p{margin-top:15px}
.steps{font-size:14px;line-height:16px;list-style:none}
.steps li{margin-top:16px;padding-left:11px;text-indent:-11px}
.steps li:nth-child(1){width:215px}
.steps li:nth-child(2){width:222px}
.steps li:nth-child(3){width:234px}
.steps li:nth-child(4){width:244px}
.steps li:nth-child(5){width:250px}
.panel-rule{position:absolute;top:0;width:1px;height:594px;background:var(--rule)}
.brand{position:absolute;left:605px;top:26px;font-weight:900;font-size:34px;letter-spacing:-.5px;color:var(--white)}
.brand-dot{display:inline-block;width:12px;height:12px;border-radius:50%;background:var(--red-bright);margin-right:8px;vertical-align:middle}
.front-line{position:absolute;left:565px;top:500px;width:270px;text-align:center;font-weight:700;font-size:14px;line-height:17px}
.small{font-size:12px;line-height:17px}
.hl{color:var(--orange)}
.caps{text-transform:uppercase}
.lead{font-weight:700;font-size:15.5px;line-height:17px;color:var(--orange)}
.loud{font-weight:700;font-size:14.5px;line-height:16px;color:var(--orange)}
.compare{position:absolute;left:12px;top:53px;width:255px;height:134px;background:var(--white)}
.compare svg{position:absolute;top:12px;width:108px;height:112px}
.compare span{position:absolute;bottom:12px;font-size:11px;font-weight:700;color:var(--white)}
</style>
</head>
<body>
<div class="stage">

  <!-- OUTER SHEET -->
  <section class="sheet sheet--outer">
    <svg class="sheet-bg" viewBox="0 0 840 594" aria-hidden="true">
      <defs>
        <linearGradient id="redPanel" x1="0" x2="1" y1="0" y2="0">
          <stop offset="0" stop-color="#e3141d"/><stop offset="1" stop-color="#a50d12"/>
        </linearGradient>
      </defs>
      <path d="M0 0H160C250 60 292 220 278 594H0Z" fill="url(#redPanel)"/>
      <path d="M160 0C250 60 292 220 278 594" fill="none" stroke="#fff" stroke-width="5"/>
    </svg>
    <div class="panel-rule" style="left:278px"></div>
    <div class="panel-rule" style="left:560px"></div>

    <div class="block" style="left:0;top:20px">
      <span class="tag tag--white">Patch Repair Process</span>
    </div>
    <ol class="block steps" style="left:11px;top:48px">
      <li>1 Clean the line with a high pressure water jetter, and carry out a camera inspec tion to determine the exact location and cause of the problems.</li>
      <li>2 Prepare the liner. Cut the liner to the correct length, mix the appropriate amount of rein and impregnate the rein into the liner.</li>
      <li>3 Invert the liner into the pipe, inflate and then cure.</li>
      <li>4 A seamless, flexible liner is cut to length and filled with environmentally safe epoxy rein. The liner is them inverted into the existing, host pipe and inflated using compressed air. Once the liner is fully cured with hot water, it is ready for use.</li>
      <li>5 The result is a completely new pipe inside the old. This pipe within a pie is 100% water tight, stronger than PVC pipe, and has an increased flow rate compared to most existing pipes. Relined pipes have a life expectancy of &nbsp;50 years and our installation work has a 25 year guarantee.</li>
    </ol>

    <div class="block" style="left:278px;top:20px"><span class="tag">What Does Pipe Relining Mean?</span></div>
    <div class="block copy" style="left:291px;top:42px;width:262px">
      <p>Pipe relining is the method of repairing existing pipework from within the pipe itself. This is done by using the latest technology to insert a strong internal liner inside the existing pipe.</p>
      <p>During this process the resin impreg-nated side of the liner is pressed against the wall of the original host pipe at a specified pressure. This pres sure ensure 100% resin contact and extrudes resin into all pipe joints, cracks and breaks ensuring no future tree root ingress or pipe movement is possible. Pipe relining can be under-taken in either short sectional repair, or long lengths utilising the inversion relining method.</p>
    </div>
    <div class="block" style="left:278px;top:373px"><span class="tag">What Does Pipe Relining Mean?</span></div>
    <div class="block copy" style="left:291px;top:390px;width:262px">
      <p>Pipe relining can repair broken, cracked or root infested pipes, pipes with missing sections and pipes that continually block.</p>
      <p>No matter if the pipes are vertical, horizontal or concealed, they all can be repaired. Sections of broken pipes can be relined, without having to re-place the entire pipeline.</p>
    </div>

    <div class="brand"><span class="brand-dot"></span>Pipewell</div>
    <svg class="block" style="left:560px;top:95px" width="280" height="400" viewBox="0 0 280 400" role="img" aria-label="Photo of a suburban house with a tree whose roots wrap around a relined drain pipe beneath the lawn">
      <defs>
        <clipPath id="photoClip"><rect x="0" y="0" width="280" height="400"/></clipPath>
        <linearGradient id="photoTone" x1="0" y1="0" x2="0" y2="1">
          <stop offset="0" stop-color="#8fb8d8"/><stop offset=".35" stop-color="#c9c3aa"/>
          <stop offset=".55" stop-color="#5f8a3a"/><stop offset=".75" stop-color="#6a4c33"/><stop offset="1" stop-color="#3d2a1c"/>
        </linearGradient>
      </defs>
      <g clip-path="url(#photoClip)">
        <circle cx="145" cy="195" r="198" fill="var(--red)"/>
        <circle cx="145" cy="188" r="190" fill="url(#photoTone)"/>
      </g>
    </svg>
    <p class="front-line">Why replace all of your drainage pipes<br>when you can permanently repair<br>the broken sections without<br>destroying your environment.</p>
  </section>

  <!-- INNER SHEET -->
  <section class="sheet sheet--inner">
    <svg class="sheet-bg" viewBox="0 0 840 594" aria-hidden="true">
      <path d="M0 52Q300 2 560 62Q690 46 840 28V540Q430 600 0 548Z" fill="#000"/>
      <path d="M0 52Q300 2 560 62Q690 46 840 28" fill="none" stroke="var(--orange)" stroke-width="6"/>
      <path d="M0 548Q430 600 840 540" fill="none" stroke="var(--orange)" stroke-width="6"/>
      <line x1="278" y1="60" x2="278" y2="555" stroke="#2a2a2a"/>
      <line x1="560" y1="65" x2="560" y2="545" stroke="#2a2a2a"/>
    </svg>

    <div class="compare">
      <svg style="left:10px" viewBox="0 0 108 112" role="img" aria-label="Camera view inside a cracked, rusty pipe before relining">
        <defs><radialGradient id="before"><stop offset="0" stop-color="#111"/><stop offset=".3" stop-color="#5a3a30"/><stop offset="1" stop-color="#b98a7a"/></radialGradient></defs>
        <rect width="108" height="112" fill="url(#before)"/>
      </svg>
      <svg style="left:133px" viewBox="0 0 108 112" role="img" aria-label="Camera view inside a smooth green relined pipe after repair">
        <defs><radialGradient id="after"><stop offset="0" stop-color="#111"/><stop offset=".3" stop-color="#2c5a1c"/><stop offset="1" stop-color="#6fd13c"/></radialGradient></defs>
        <rect width="108" height="112" fill="url(#after)"/>
      </svg>
      <span style="left:15px">Before</span><span style="left:138px">After</span>
    </div>

    <div class="block" style="left:0;top:207px"><span class="tag" style="padding-left:23px;padding-right:40px">Benefits of Pipe Relining</span></div>
    <div class="block small" style="left:23px;top:236px;width:245px;font-size:13px">
      <p><span class="hl">Quick Installation</span> – Most relining jobs can be completed in the same day-without tht mess and disruption of excavation.</p>
      <p><span class="hl">Long Life Product</span> – Pipe Relining is a long term solution with a 50 year life expectancy.</p>
      <p><span class="hl">Minimal Disruption</span> – ave your landscapes, trees and driveways.</p>
      <p><span class="hl">Economical</span> – Save on the cost, time and hassle of restoring your property and landscaping.</p>
      <p><span class="hl">Installation Guarantee</span> – Pipewell offer a 25 year warranty, twice that of standard ex-cavations. This also includes an annual warranty camera inspection.</p>
    </div>

    <p class="block lead" style="left:291px;top:72px;width:250px">Provides a solution to the whole problem, not just temporary relief from the symptoms.</p>
    <div class="block" style="left:278px;top:138px"><span class="tag">What Does Pipe Relining Mean?</span></div>
    <div class="block small" style="left:291px;top:165px;width:255px;font-size:13px">
      Permanent jointless liner<br>50 years life expectancy<br>Up front price<br>Environmentally sound<br>Eliminates structural disturbances<br>Imprevious to future root penetration<br>Provides increased flow characteristics<br>Suitable for industrial, residential and com-mercial applications
    </div>
    <div class="block" style="left:278px;top:339px"><span class="tag" style="padding-right:60px">Things You Should Know</span></div>
    <div class="block small" style="left:291px;top:366px;width:255px">
      <p class="hl" style="font-size:13px">Knowledge &amp; Experience</p>
      <p>We train other plumbers and have been doing it for over 10 years.</p>
      <p class="hl" style="font-size:13px;margin-top:2px">We’re An Owned &amp; Operated Business</p>
      <p>We take great pride in our work. Our business is based on relationships not transactions.</p>
      <p class="loud caps" style="margin-top:6px">We use the best in class pipe re-lining solution</p>
      <p>We have sourced the best products and equip-ment from around the world and our Re-Flow product is from Germany.</p>
    </div>

    <div class="block" style="left:562px;top:62px"><span class="tag" style="padding-right:30px">Why It Works:</span></div>
    <div class="block small" style="left:575px;top:95px;width:255px">
      <p class="caps">Pipewell uses epoxy rein not poly-ester or silicate resins.</p>
      <p style="margin-top:17px">Why? Because epoxy resin does not shrink. Polyester and silicate resins can shrink in the pipe allowing tree roots to return.</p>
      <p class="caps" style="margin-top:17px">Pipewell inverts th eliner instead of using a drag-in method.</p>
      <p style="margin-top:17px">Why? Because this means that the resin has contact with the host pipe impregnating the cracks and joins the pipework. With the drag in method, the resin does not have contact with the host pipe and cannot impregnate the cracks and joins.</p>
      <p class="caps" style="margin-top:17px">Pipewell uses a German system called Kellinor.</p>
      <p style="margin-top:17px">Why? Because it has been extensively tested in Europe and came out as the test winner in standard and extreme conditions based on all assessment criteria – effectiveness, density and load carrying capacity. Kellinor has a proven</p>
    </div>
  </section>

</div>
</body>
</html>
```